Red Gum Business Card Design

We are a new small business specialising in under ground cable jointing and excavation works in NSW Australia.
Design I'm looking for is incorporating the Australian flag & excavator with out being to cheesy.
Maybe a faded washed out flag to help with overload of colour? & so its not the main focus.
Very open to creative out of the box designs!

Target Market(s)

Building & Construction

Industry/Entity Type

Construction

Contact Information for Business Card

Red Gum Cable Jointing & Excavations
Owen Falkirk

Ph: 0438 605 312
E: owen.falkirk@tallmail.example

Reverse Side
Services we offer:
High Voltage & Low Voltage Cable Jointing
Polymeric & paperlead jointing & terminations
Trenching & Auger Drilling 150 - 600mm
Site preparation / leveling / clearing
Driveway / Footpath / Turf Prep
Rubbish Removal
Tree & Stump removal
Footings & Post holes
Drainage
Service Installs
Gravels & Sands available
Any general Earth moving needs
Reliable Free Quotes
Fully Insured

Font styles to use
Serif
Script

Requirements
Nice to have
• small excavator (See uploaded picture)

```html
<!DOCTYPE html>
<html lang="en">
<head>
<meta charset="utf-8">
<title>Red Gum Cable Jointing &amp; Excavations – Business Card</title>
<link rel="stylesheet" href="https://fonts.googleapis.com/css2?family=Arimo:wght@400;500&display=swap">
<style>
  :root {
    --card-yellow: #fdd400;
    --card-grey: #5b5b5b;
    --card-grey-deep: #4a4a4a;
    --name-plate: #2f2d2d;
    --ink: #3a3a3a;
    --white: #ffffff;
    --page: #ffffff;
  }
  * { margin: 0; padding: 0; box-sizing: border-box; }
  html, body {
    width: 1200px;
    height: 741px;
    overflow: hidden;
    background: var(--page);
    font-family: "Arimo", Arial, sans-serif;
  }
  .business-card {
    position: absolute;
    left: 44px;
    top: 44px;
    width: 1121px;
    height: 656px;
    background: var(--card-grey);
    box-shadow: 0 18px 30px rgba(0,0,0,0.28), 0 2px 6px rgba(0,0,0,0.15);
    overflow: hidden;
  }
  .card-panels {
    position: absolute;
    inset: 0;
    width: 100%;
    height: 100%;
  }
  .name-plate {
    position: absolute;
    left: 66px;
    top: 217px;
    width: 315px;
    height: 86px;
    background: var(--name-plate);
    color: var(--white);
    font-size: 35px;
    font-weight: 400;
    display: flex;
    align-items: center;
    justify-content: center;
    letter-spacing: 0.2px;
  }
  .contact-details {
    position: absolute;
    left: 67px;
    top: 330px;
    color: var(--ink);
    font-size: 20px;
    font-weight: 500;
    list-style: none;
    line-height: 40px;
  }
  .excavator-image {
    position: absolute;
    left: 559px;
    top: 52px;
    width: 491px;
    height: 395px;
    border-radius: 30px 60px 20px 20px;
    background: radial-gradient(ellipse at 60% 55%, #f2a51c 0%, #e19a1a 35%, rgba(40,40,40,0.9) 75%, rgba(91,91,91,0) 100%);
  }
  .company-label {
    position: absolute;
    left: 632px;
    top: 467px;
    width: 420px;
    height: 116px;
    border: 7px solid var(--card-yellow);
    background: linear-gradient(180deg, #ffffff 0%, #efefef 55%, #d4d4d4 100%);
    display: flex;
    align-items: center;
    justify-content: center;
    text-align: center;
    color: #111111;
    font-size: 31px;
    line-height: 38px;
    font-weight: 400;
  }
</style>
</head>
<body>
  <article class="business-card">
    <svg class="card-panels" viewBox="0 0 1121 656" preserveAspectRatio="none" aria-hidden="true">
      <defs>
        <linearGradient id="edge-shade" x1="0" y1="0" x2="1" y2="0">
          <stop offset="0" stop-color="#000" stop-opacity="0.35"/>
          <stop offset="1" stop-color="#000" stop-opacity="0"/>
        </linearGradient>
      </defs>
      <polygon points="559,0 600,0 368,656 327,656" fill="url(#edge-shade)"/>
      <polygon points="0,0 559,0 327,656 0,656" fill="var(--card-yellow)"/>
    </svg>

    <h1 class="name-plate">Owen Falkirk</h1>

    <ul class="contact-details">
      <li class="contact-phone">Ph: 0438 605 312</li>
      <li class="contact-email">E: owen.falkirk@tallmail.example</li>
    </ul>

    <div class="excavator-image" role="img" aria-label="Yellow compact tracked excavator with black bucket"></div>

    <p class="company-label">Red Gum Cable<br>Jointing and Excavations</p>
  </article>
</body>
</html>
```